Your Health, Your Time, Your Way: Personalized, Concierge Care Elevated to Modern Medicine

We need to incorporate an image of our new doctor (Dr. Marlene Quorvath, MD) with our office logo ( Bright Harbor Clinic) and dialogue that shows how simple it is to schedule a free consult and learn what our office has to offer patients. The colors should be consistent with our website- the CMYK codes will be attached for your use below. The font should be easy to read. The text should be clear, and convey value to the patient for chosing us over anyone else ( we offer primary care, preventive medicine, urgen care and functional medicine with 24 hour direct access to care with some of our strengths including focus on individualized care, cutting edge medicine, blended functional and traditional style. We aim to transform lives through patient centered innovative and individualized care plan. I have attached a "mock" image but the details ( office address, name, phone number are incorrect) The correct info is Bright Harbor Clinic 4187 Pellman Ave Suite 214, Clearwater, FL 33798 and phone number (727)555-0148. A possible hook could read: welcoming new patients now- Your Health, Your Time, Your Way: Personalized Care Meets Modern Medicine
Updates

I did not realize that there was a tab with more information to fill for the designers to see, or for me to upload the basic information they need to create the design.

Target Market(s)

Patients over 18 years of age with interest in longevity, functional and traditional medicine; the postcards will be mailed to our CURRENT patients, and they are a reminder of what we do, new patient availability AND a request for them to refer friends or families

Industry/Entity Type

medical

Font styles to use
Sans Serif

Colors

Designer to choose colors to be used in the design.

Requirements
Must have
• simple reminder to current patients of what we offer, and a call to action for our patients to refer friends and family for same level of excellence;consistency with brand ( see business card and cmyx codes for colors);photo of new physician; logo Bright Harbor Clinic, web site (https://brightharborclinic.example); Must clearly express accepting new patients; simple to call/email to schedule free consultation;; include our email (frontdesk@brightharborclinic.example), phone number (727)555-0148; our address 4187 Pellman Ave Suite 214, Clearwater, FL 33798
Nice to have
• photo of our new physician ( in blue jacket: Dr. Marlene Quorvath, MD) should not take up too much space
Should not have
• clutter, or close text; full sentences( bulleted text preferred)

```html
<!DOCTYPE html>
<html lang="en">
<head>
<meta charset="utf-8">
<title>Bright Harbor Clinic – Welcoming New Patients</title>
<link href="https://fonts.googleapis.com/css2?family=Montserrat:wght@400;500;600;700;900&display=swap" rel="stylesheet">
<style>
  :root{
    --stage:#222222;
    --paper:#ffffff;
    --orange:#e8801f;
    --teal:#4a7580;
    --ink:#1c1c1c;
    --white:#ffffff;
    --portrait-a:#2a2f45;
    --portrait-b:#141a2e;
  }
  *{margin:0;padding:0;box-sizing:border-box}
  html,body{width:1200px;height:1200px;overflow:hidden;background:var(--stage)}
  body{font-family:"Montserrat",sans-serif;position:relative}
  .postcard{position:absolute;left:54px;top:296px;width:1092px;height:607px;background:var(--orange);overflow:hidden}
  .header-band{position:absolute;left:0;top:0;width:100%;height:183px;background:var(--paper)}
  .brand{position:absolute;left:30px;top:38px;width:175px;display:flex;align-items:center;gap:10px}
  .brand-dot{width:22px;height:22px;border-radius:50%;background:var(--ink);flex:none}
  .brand-name{font-weight:600;font-size:25px;line-height:1.15;color:var(--ink)}
  .divider-v{position:absolute;left:221px;top:9px;height:162px;border-left:1px dashed #9a9a9a}
  .contact{position:absolute;left:258px;top:15px;color:var(--ink);font-weight:500;font-size:25px;line-height:28px}
  .contact-row{display:flex;align-items:flex-start;gap:6px}
  .contact-row svg{flex:none;margin-top:3px}
  .address{margin-top:4px}
  .headline{position:absolute;left:260px;top:110px;font-weight:900;font-size:35px;line-height:31px;color:var(--teal);letter-spacing:.3px}
  .content{position:absolute;left:42px;top:190px;width:410px;color:var(--white)}
  .section-title{font-weight:700;font-size:23px;line-height:28px}
  .service-grid{display:grid;grid-template-columns:159px auto;row-gap:2px;margin-top:6px;font-size:19.5px;line-height:23px}
  .tick-item{display:flex;align-items:flex-start;gap:5px}
  .tick-item svg{flex:none;margin-top:5px}
  .rule{border-top:1px solid rgba(255,255,255,.85);margin:12px 0}
  .access{font-weight:700;font-size:22px;line-height:26px}
  .strengths{margin-top:4px;font-size:19.5px;line-height:25px}
  .mission{font-size:19px;line-height:25px;color:var(--ink)}
  .photo-area{position:absolute;left:0;top:0;width:1092px;height:607px}
  .name-band{position:absolute;left:495px;top:523px;width:535px;height:84px;display:flex;flex-direction:column;align-items:center;justify-content:center;text-align:center}
  .doctor-name{font-weight:700;font-size:28px;line-height:32px;color:var(--ink);letter-spacing:.2px}
  .cta-line{font-weight:600;font-size:12.5px;line-height:17px;color:var(--white)}
</style>
</head>
<body>
<div class="postcard">
  <div class="header-band"></div>

  <svg class="photo-area" viewBox="0 0 1092 607">
    <defs>
      <clipPath id="lower-field"><rect x="0" y="183" width="1092" height="424"/></clipPath>
      <linearGradient id="portrait-tone" x1="0" y1="0" x2="0" y2="1">
        <stop offset="0" stop-color="#4a3630"/>
        <stop offset="0.5" stop-color="var(--portrait-a)"/>
        <stop offset="1" stop-color="var(--portrait-b)"/>
      </linearGradient>
    </defs>
    <circle cx="778" cy="500" r="280" fill="var(--paper)" clip-path="url(#lower-field)"/>
    <path role="img" aria-label="Portrait photo of Dr. Marlene Quorvath in a navy blazer" d="M765 12 Q705 12 705 80 L705 270 Q705 300 665 320 Q623 342 623 400 L623 526 L1048 526 L1048 400 Q1048 335 1000 305 L1000 80 Q1000 12 940 12 Z" fill="url(#portrait-tone)"/>
    <polygon points="495,523 1045,523 1014,607 495,607" fill="var(--teal)"/>
  </svg>

  <div class="brand">
    <span class="brand-dot"></span>
    <span class="brand-name">Bright Harbor Clinic</span>
  </div>
  <div class="divider-v"></div>

  <div class="contact">
    <div class="contact-row">
      <svg width="20" height="22" viewBox="0 0 24 24"><path d="M6.6 10.8a15 15 0 0 0 6.6 6.6l2.2-2.2a1 1 0 0 1 1-.25 11.4 11.4 0 0 0 3.6.57 1 1 0 0 1 1 1V20a1 1 0 0 1-1 1A17 17 0 0 1 3 4a1 1 0 0 1 1-1h3.5a1 1 0 0 1 1 1c0 1.25.2 2.450.57 3.57a1 1 0 0 1-.25 1z" fill="var(--orange)"/></svg>
      <span>(727)555-0148</span>
    </div>
    <div class="contact-row address">
      <svg width="20" height="24" viewBox="0 0 24 28"><path d="M12 2a7 7 0 0 0-7 7c0 5 7 12 7 12s7-7 7-12a7 7 0 0 0-7-7zm0 9.5A2.5 2.5 0 1 1 12 6.5a2.5 2.5 0 0 1 0 5z" fill="var(--orange)"/><ellipse cx="12" cy="24" rx="7" ry="2" fill="none" stroke="var(--orange)" stroke-width="1.5"/></svg>
      <span>4187 Pellman Ave Suite 214,<br>Clearwater, FL 33798</span>
    </div>
  </div>

  <h1 class="headline">WELCOMING NEW<br>PATIENTS NOW</h1>

  <div class="content">
    <h2 class="section-title">Services Offered:</h2>
    <div class="service-grid">
      <div class="tick-item"><svg width="14" height="14" viewBox="0 0 16 16"><circle cx="8" cy="8" r="7" fill="none" stroke="#fff" stroke-width="1.2"/><path d="M5 8.2l2 2 4-4" fill="none" stroke="#fff" stroke-width="1.2"/></svg>Primary Care</div>
      <div class="tick-item"><svg width="14" height="14" viewBox="0 0 16 16"><circle cx="8" cy="8" r="7" fill="none" stroke="#fff" stroke-width="1.2"/><path d="M5 8.2l2 2 4-4" fill="none" stroke="#fff" stroke-width="1.2"/></svg>Preventive Medicine</div>
      <div class="tick-item"><svg width="14" height="14" viewBox="0 0 16 16"><circle cx="8" cy="8" r="7" fill="none" stroke="#fff" stroke-width="1.2"/><path d="M5 8.2l2 2 4-4" fill="none" stroke="#fff" stroke-width="1.2"/></svg>Urgent Care</div>
      <div class="tick-item"><svg width="14" height="14" viewBox="0 0 16 16"><circle cx="8" cy="8" r="7" fill="none" stroke="#fff" stroke-width="1.2"/><path d="M5 8.2l2 2 4-4" fill="none" stroke="#fff" stroke-width="1.2"/></svg>Functional Medicine</div>
    </div>
    <div class="rule"></div>
    <p class="access">We provide round-the-clock,<br>direct access to care.</p>
    <div class="rule"></div>
    <h2 class="section-title">Our Strengths:</h2>
    <div class="strengths">
      <div class="tick-item"><svg width="14" height="14" viewBox="0 0 16 16"><circle cx="8" cy="8" r="7" fill="none" stroke="#fff" stroke-width="1.2"/><path d="M5 8.2l2 2 4-4" fill="none" stroke="#fff" stroke-width="1.2"/></svg>Emphasis on individualized care plans.</div>
      <div class="tick-item"><svg width="14" height="14" viewBox="0 0 16 16"><circle cx="8" cy="8" r="7" fill="none" stroke="#fff" stroke-width="1.2"/><path d="M5 8.2l2 2 4-4" fill="none" stroke="#fff" stroke-width="1.2"/></svg>Use of cutting-edge medical practices.</div>
      <div class="tick-item"><svg width="14" height="14" viewBox="0 0 16 16"><circle cx="8" cy="8" r="7" fill="none" stroke="#fff" stroke-width="1.2"/><path d="M5 8.2l2 2 4-4" fill="none" stroke="#fff" stroke-width="1.2"/></svg>A blend of functional and traditional<br>medical approaches.</div>
    </div>
    <div class="rule"></div>
    <p class="mission">Transforming lives through innovative,<br>patient-centered care plans tailored to<br>each individual’s unique needs.</p>
  </div>

  <div class="name-band">
    <div class="doctor-name">DR. MARLENE QUORVATH, MD</div>
    <div class="cta-line">Call or email for a free consult · Refer friends &amp; family</div>
    <div class="cta-line">frontdesk@brightharborclinic.example · brightharborclinic.example</div>
  </div>
</div>
</body>
</html>
```